Professional Consulting Firm Business Card Design

We need a business card design for a new professional consulting firm that specializes in petroleum, health, and financial consulting. We need a design that is trendy but elegant, and one that would make a vantage 300 executive feel comfortable using our services. I have attached a logo that needs to be used in the design. I have also attached a photo of a card design that I like.

On the card we need a place for employee name, title, email address, fax number, phone number, mailing address, and website address.

Industry/Entity Type

Financial

Contact Information for Business Card

see attached

Font styles to use
Other font styles liked:
• Calibri or your choice

Requirements
Must have
• style
Nice to have
• texture, rounded edges
Should not have
• no solid black cards but black may be used

```html
<!DOCTYPE html>
<html lang="en">
<head>
<meta charset="utf-8">
<title>Meridian Consulting LLC – Business Card</title>
<link href="https://fonts.googleapis.com/css2?family=Tinos:wght@400;700&display=swap" rel="stylesheet">
<style>
  :root {
    --navy: #134a7c;
    --ink: #2a2a2a;
    --paper: #ffffff;
    --mist: #b7bdd2;
    --backdrop: #4b4b4d;
  }
  * { margin: 0; padding: 0; box-sizing: border-box; }
  html, body { width: 1200px; height: 1000px; overflow: hidden; }
  body {
    background: var(--backdrop);
    font-family: "Tinos", "Times New Roman", serif;
    position: relative;
  }
  .card {
    position: absolute;
    width: 546px;
    height: 320px;
    overflow: hidden;
  }
  /* Front */
  .card--front {
    left: 91px; top: 134px;
    background: var(--navy);
  }
  .front-brand {
    position: absolute;
    left: 0; right: 0; top: 0; bottom: 0;
    display: flex; align-items: center; justify-content: center;
    gap: 14px;
    color: var(--paper);
  }
  .front-brand__mark {
    width: 14px; height: 14px; background: var(--paper);
  }
  .front-brand__name {
    font-size: 30px; letter-spacing: 1px;
  }
  /* Back */
  .card--back {
    left: 545px; top: 550px;
    background: var(--paper);
  }
  .holder { position: absolute; left: 43px; top: 48px; }
  .holder__name { color: var(--navy); font-size: 18px; line-height: 22px; }
  .holder__title { color: var(--ink); font-size: 14px; line-height: 18px; }
  .back-brand {
    position: absolute; right: 36px; top: 50px;
    display: flex; align-items: center; gap: 9px;
    color: var(--navy);
  }
  .back-brand__mark { width: 10px; height: 10px; background: var(--navy); }
  .back-brand__name { font-size: 19px; letter-spacing: 0.5px; }
  .contacts {
    position: absolute; right: 40px; top: 112px;
    list-style: none; text-align: right;
  }
  .contacts li {
    display: flex; justify-content: flex-end; align-items: center;
    gap: 7px; font-size: 14px; line-height: 19px; color: var(--ink);
  }
  .contacts svg { width: 14px; height: 14px; fill: none; stroke: var(--navy); stroke-width: 1.6; }
  .address {
    position: absolute; right: 40px; top: 211px;
    text-align: right; font-style: normal;
    font-size: 14px; line-height: 17.5px; color: var(--ink);
  }
  .address__company { color: var(--navy); }
  .watermark-name {
    position: absolute; left: 42px; top: 185px;
    font-size: 58px; color: var(--mist); letter-spacing: 1px;
  }
  .band {
    position: absolute; left: 0; right: 0; bottom: 0; height: 26px;
    background: var(--navy);
  }
</style>
</head>
<body>

<section class="card card--front" aria-label="Card front">
  <div class="front-brand">
    <span class="front-brand__mark"></span>
    <span class="front-brand__name">MERIDIAN CONSULTING LLC</span>
  </div>
</section>

<section class="card card--back" aria-label="Card back">
  <div class="holder">
    <p class="holder__name">Daniel Hart</p>
    <p class="holder__title">President</p>
  </div>

  <div class="back-brand">
    <span class="back-brand__mark"></span>
    <span class="back-brand__name">MERIDIAN CONSULTING LLC</span>
  </div>

  <ul class="contacts">
    <li>555 018 2740
      <svg viewBox="0 0 16 16"><path d="M4 2l2.5 3-1.5 1.5a9 9 0 0 0 4.5 4.5L11 9.5l3 2.5-1.5 2.5C7 14 2 9 1.5 3.5z"/></svg>
    </li>
    <li>555 018 2741
      <svg viewBox="0 0 16 16"><rect x="4" y="1.5" width="8" height="4"/><rect x="1.5" y="5.5" width="13" height="6" rx="1"/><rect x="4" y="9.5" width="8" height="5"/></svg>
    </li>
    <li>info@meridianconsult.com
      <svg viewBox="0 0 16 16"><rect x="1.5" y="3.5" width="13" height="9"/><path d="M1.5 3.5L8 9l6.5-5.5"/></svg>
    </li>
    <li>www.meridianconsult.com
      <svg viewBox="0 0 16 16"><circle cx="8" cy="8" r="6.5"/><path d="M1.5 8h13M8 1.5c-3 3.5-3 9.5 0 13M8 1.5c3 3.5 3 9.5 0 13"/></svg>
    </li>
  </ul>

  <address class="address">
    <span class="address__company">MERIDIAN CONSULTING LLC.</span><br>
    Suite 410, 18 Linden Avenue,<br>
    Opposite to Calder Plaza, New York,<br>
    NY 10012
  </address>

  <div class="watermark-name">Meridian</div>

  <div class="band"></div>
</section>

</body>
</html>
```